Used Car Dealer seeks an Amazing Business Card Design

We are looking for a business card design that incorporates our logo and grabs the attention of anyone we give the business card to.

Looking to use the same colors as the logo. Our Logo choice is the black background with Red and Silver/Grey Lettering.

We also would like to see some embossed designs.

Target Market(s)

Used Car Buyers, Automotive, Auto

Industry/Entity Type

Automotive

Contact Information for Business Card

BVEL7K
Gordon Whitlock
482 Tarrow Lane
Suite 207
Halvern, XR 00418
Office (555) 555-0142
Cell (555) 555-0187
bvel7kga@quellmail.com
www.bvel7kga.com

Colors
ffffff
ee3036

Requirements
Must have
• Must include our logo (Black Background with Red and Silver/Grey Lettering)
Nice to have
• Embossed Design. Can be Single or Double Sided.

```html
<!DOCTYPE html>
<html lang="en">
<head>
<meta charset="utf-8">
<title>BVEL7K Business Card</title>
<link href="https://fonts.googleapis.com/css2?family=Cinzel:wght@500&family=Open+Sans:wght@400;700&display=swap" rel="stylesheet">
<style>
  :root {
    --stage: #a9a9ad;
    --card-black: #1c1c1d;
    --card-white: #f7f8fa;
    --red: #ee3036;
    --silver: #c9cacd;
    --grey-text: #5a5b5e;
    --rule: #8c8d90;
  }
  * { margin: 0; padding: 0; box-sizing: border-box; }
  html, body { width: 1200px; height: 863px; overflow: hidden; }
  body {
    background: var(--stage);
    font-family: "Open Sans", sans-serif;
    position: relative;
  }
  .card {
    position: absolute;
    width: 540px;
    height: 309px;
    top: 277px;
    overflow: hidden;
  }
  .card-front { left: 40px; background: var(--card-black); }
  .card-back { left: 620px; background: var(--card-white); }

  .wordmark {
    font-family: "Open Sans", sans-serif;
    font-weight: 700;
    letter-spacing: 1px;
  }
  .card-front .wordmark {
    position: absolute;
    left: 0; right: 0; top: 118px;
    text-align: center;
    font-size: 56px;
    line-height: 1;
    color: var(--silver);
  }
  .card-back .wordmark {
    position: absolute;
    left: 40px; top: 34px;
    font-size: 34px;
    line-height: 1;
    color: var(--grey-text);
  }
  .divider {
    position: absolute;
    left: 40px; top: 96px;
    width: 330px; height: 1px;
    background: var(--rule);
  }
  .contact-list {
    position: absolute;
    left: 40px; top: 120px;
    list-style: none;
    font-size: 12.5px;
    line-height: 19px;
    color: var(--grey-text);
  }
  .contact-list li { display: flex; align-items: center; gap: 8px; }
  .contact-list svg { width: 10px; height: 10px; flex: none; }
  .person {
    position: absolute;
    right: 40px; top: 196px;
    text-align: right;
  }
  .person-name {
    font-family: "Cinzel", serif;
    font-weight: 500;
    font-size: 21px;
    color: var(--red);
    letter-spacing: 0.5px;
    padding-bottom: 2px;
    border-bottom: 1px solid var(--rule);
  }
  .person-role {
    font-size: 12.5px;
    color: var(--grey-text);
    margin-top: 2px;
  }
  .company {
    position: absolute;
    right: 40px; top: 246px;
    text-align: right;
    color: var(--grey-text);
  }
  .company-name { font-weight: 700; font-size: 15px; }
  .company-address { font-size: 11.5px; margin-top: 2px; }
  .edge-band {
    position: absolute;
    left: 0; right: 0; bottom: 0;
    height: 6px;
    background: var(--red);
  }
</style>
</head>
<body>
  <section class="card card-front">
    <div class="wordmark">BVEL7K</div>
  </section>

  <section class="card card-back">
    <div class="wordmark">BVEL7K</div>
    <div class="divider"></div>
    <ul class="contact-list">
      <li>
        <svg viewBox="0 0 10 10" aria-hidden="true"><path d="M2 1 L4 1 L4.6 3 L3.4 3.8 Q4.4 5.8 6.2 6.6 L7 5.4 L9 6 L9 8 Q8 9 6.5 8.6 Q2.5 7 1.2 3 Q1 1.8 2 1 Z" fill="var(--red)"/></svg>
        (555) 555-0187 or (555) 555-0142
      </li>
      <li>
        <svg viewBox="0 0 10 10" aria-hidden="true"><rect x="0.8" y="2" width="8.4" height="6" fill="none" stroke="var(--red)" stroke-width="1.2"/><path d="M1 2.4 L5 5.4 L9 2.4" fill="none" stroke="var(--red)" stroke-width="1.2"/></svg>
        bvel7kga@quellmail.com
      </li>
      <li>
        <svg viewBox="0 0 10 10" aria-hidden="true"><circle cx="6" cy="4" r="3" fill="none" stroke="var(--red)" stroke-width="1.3"/><path d="M3.8 6.2 L1 9" stroke="var(--red)" stroke-width="1.5"/></svg>
        www.bvel7kga.com
      </li>
    </ul>
    <div class="person">
      <div class="person-name">GORDON WHITLOCK</div>
      <div class="person-role">Owner</div>
    </div>
    <div class="company">
      <div class="company-name">BVEL7K</div>
      <div class="company-address">482 Tarrow Lane, Suite 207, Halvern, XR 00418</div>
    </div>
    <div class="edge-band"></div>
  </section>
</body>
</html>
```